New design for a physiotherapy clinic specializing in laser therapy

BrightPath Physiotherapy is a unique clinic specializing in laser therapy. The clinic is now 7 years old and has a well established reputation for patient care.

We are the largest laser physiotherapy clinic in Mississauga, ON, Canada. We use state of the art laser therapy equipment. Our knowledge base of how to use Low Level Laser Therapy in conjunction with traditional physiotherapy is what sets us apart. Nobody wants to live with pain and everyone wants to get better as quickly as possible. Our treatment methodology helps our patients return to normal lives quickly.

We want a website that communicates expertise, trust and shows that we care for our patients. We also want people to understand that the treatments are painless and speed up healing naturally.
Updates

Please include a location tab in your submission.  This page should have a map of our location and our phone number.

I do not want any white coat and stethoscope people. We do not see hospitalized patients. We use Vara-Kor NuvoTel laser web site www.nuvotelbeam.example please remove any images with other laser machines. I do not want "massage" therapy pictures as the main image. We treat post op total hip and knee replacements, rotator cuff injuries, osteoarthritic back pain patients, sprained ankles, degenerative disc disease problems as some of the more general injuries seen.

Industry/Entity Type

Clinic

Requirements
Must have
• We want to retain as much of the current content as possible. We will be looking at editing the content to make it shorter.

In addition to the current pages we want to add a blog page and link.

see our current site www.brightpathphysio.example
Nice to have
• Medical Images in the Whiplash and Auto Injuries should be re-drawn.

We want a clean, uncluttered look to the site.

Should not have
• Do not use illustrations of lasers shooting out or cutting. This is a "Cold" laser and does not cut. The laser procedure is gentle and soothing.

```html
<!DOCTYPE html>
<html lang="en">
<head>
<meta charset="utf-8">
<title>BrightPath Physiotherapy Inc.</title>
<link href="https://fonts.googleapis.com/css2?family=Open+Sans:wght@400;600;700&display=swap" rel="stylesheet">
<style>
:root{
  --green:#5fae23;
  --green-light:#7cc242;
  --green-dark:#4a9419;
  --ink:#2f2f2f;
  --body:#8a8a8a;
  --rule:#c9c9c9;
  --hero-bar:#1d1d1d;
  --white:#ffffff;
}
*{box-sizing:border-box;margin:0;padding:0}
html,body{width:1200px;height:2405px;overflow:hidden;background:var(--white)}
body{font-family:"Open Sans",Arial,sans-serif;color:var(--ink);position:relative}
.page{position:relative;width:1200px;height:2405px}

/* header */
.brand{position:absolute;left:19px;top:56px;font-size:34px;font-weight:600;color:var(--ink);line-height:1.2;white-space:nowrap}
.top-links{position:absolute;right:16px;top:32px;font-size:17px;color:var(--green);font-weight:600}
.top-links span{color:var(--green);margin:0 4px}
.phone{position:absolute;right:16px;top:76px;display:flex;align-items:center;gap:12px;font-size:30px;font-weight:600;color:var(--ink)}

/* nav */
.main-nav{position:absolute;left:0;top:160px;width:1200px;height:43px;background:linear-gradient(var(--green-light),var(--green));display:flex}
.main-nav a{flex:auto;color:var(--white);text-decoration:none;font-size:17px;font-weight:600;text-align:center;line-height:43px;border-right:2px solid rgba(255,255,255,.85)}
.main-nav a:last-child{border-right:none}

/* hero */
.hero{position:absolute;left:0;top:206px;width:1200px;height:404px;display:flex;gap:6px;background:var(--hero-bar)}
.hero-photo{flex:1;height:100%}
.p1{background:linear-gradient(160deg,#e9d4c6,#c98f74 60%,#f1ece8)}
.p2{background:linear-gradient(180deg,#b9b2a9,#d9b39a 55%,#8e8378)}
.p3{background:linear-gradient(150deg,#2a1a12,#d25a1f 45%,#f29a45 60%,#5a3525)}
.p4{background:linear-gradient(180deg,#d6d6d6,#c8a289 55%,#4b5a6b)}
.hero-title{position:absolute;right:24px;top:520px;font-size:54px;color:var(--white);font-weight:400;letter-spacing:1px;line-height:1.2}
.hero-bar{position:absolute;left:0;top:610px;width:1200px;height:53px;background:var(--hero-bar);display:flex;justify-content:center;align-items:center;gap:22px}
.hero-bar i{width:16px;height:16px;border-radius:50%;background:var(--white)}
.hero-bar i.on{background:var(--green-light)}

/* welcome */
.welcome-title{position:absolute;left:19px;top:700px;font-size:26px;font-weight:600;color:var(--green)}
.welcome-photo{position:absolute;left:19px;top:754px;width:342px;height:235px;background:linear-gradient(180deg,#b9d6ee,#eef3f6 55%,#7aa35c)}
.welcome-text{position:absolute;left:400px;top:745px;width:780px;font-size:15.5px;line-height:1.62;color:var(--body)}
.welcome-text p+p{margin-top:26px}

.divider{position:absolute;left:19px;width:1162px;border-top:2px dashed var(--rule)}

/* columns */
.col{position:absolute;width:342px}
.col h2{font-size:21px;font-weight:600;color:var(--green);text-transform:uppercase;height:36px}
.col-photo{width:342px;height:233px}
.col p{font-size:14.5px;line-height:1.7;color:var(--body);margin-top:24px}
.col p+p{margin-top:24px}
.btn{display:inline-block;position:absolute;left:0;width:134px;height:40px;line-height:40px;text-align:center;background:linear-gradient(var(--green-light),var(--green-dark));color:var(--white);font-size:16px;font-weight:700;border-radius:7px;text-decoration:none}
.cite{font-size:14.5px;color:var(--body);margin-top:22px}

.ph-laser{background:linear-gradient(135deg,#3b4a55,#f0f2f3 50%,#d6a48b)}
.ph-massage{background:linear-gradient(180deg,#e9c8a8,#c48a60 60%,#f3e7da)}
.ph-exercise{background:linear-gradient(135deg,#e7e7e7,#2b8f7a 45%,#cfcfcf)}
.ph-insurance{background:linear-gradient(160deg,#f2f2f2,#bfbfbf 50%,#7a7a7a)}
.ph-testimonial{background:linear-gradient(180deg,#dfe6ec,#f4f4f4 50%,#b9c6cf)}

/* blog */
.post{position:absolute;left:0;width:342px}
.post h3{font-size:18px;font-weight:400;color:var(--ink)}
.post p{font-size:14.5px;line-height:1.6;color:var(--body);margin-top:10px}
.share{display:flex;gap:8px;margin-top:16px}
.share span{display:inline-block;height:20px;padding:0 6px;border:1px solid #c6cbd3;border-radius:3px;font-size:12px;line-height:18px;color:#444;background:#f3f4f6}

/* footer */
.footer-rule{position:absolute;left:0;top:2297px;width:1200px;border-top:2px solid #555}
.footer-links{position:absolute;left:12px;top:2313px;font-size:15.5px;color:var(--ink);font-weight:600}
.footer-links span{color:var(--green);margin:0 7px}
.footer-bar{position:absolute;left:0;top:2352px;width:1200px;height:53px;background:linear-gradient(var(--green-light),var(--green))}
.copyright{position:absolute;left:14px;top:16px;color:var(--white);font-size:14px}
.social{position:absolute;right:14px;top:10px;display:flex;gap:8px}
.social i{width:32px;height:32px;background:#4f4f4f;border-radius:3px}
</style>
</head>
<body>
<div class="page">

<header>
  <div class="brand">BrightPath Physiotherapy Inc.</div>
  <div class="top-links">Clinic Hours <span>|</span> Visiting Our Clinic <span>|</span> Employment Opportunities <span>|</span> Patient Forms</div>
  <div class="phone">
    <svg width="40" height="40" viewBox="0 0 40 40" aria-hidden="true"><circle cx="20" cy="20" r="19" fill="#5fae23"/><path d="M13 11c2-1 3 0 4 3l1 2c0 2-2 2-2 3 1 3 3 5 6 6 1 0 1-2 3-2l2 1c3 1 4 2 3 4-1 2-3 3-5 3-8-1-14-7-15-15 0-2 1-4 3-5z" fill="#fff"/></svg>
    905-555-0148
  </div>
</header>

<nav class="main-nav">
  <a>CLINIC HOURS</a><a>PHYSIOTHERAPY</a><a>LASER THERAPY</a><a>FAQ'S</a><a>MASSAGE THERAPY</a><a>INSURANCE</a><a>TESTIMONIALS</a><a>LOCATION</a><a>BLOG</a>
</nav>

<section class="hero">
  <div class="hero-photo p1" role="img" aria-label="Patient holding an injured knee"></div>
  <div class="hero-photo p2" role="img" aria-label="Hands resting on a sore knee"></div>
  <div class="hero-photo p3" role="img" aria-label="Hand on a painful glowing shoulder"></div>
  <div class="hero-photo p4" role="img" aria-label="Person holding a sore lower back"></div>
</section>
<div class="hero-title">Treating You Better</div>
<div class="hero-bar"><i class="on"></i><i></i><i></i><i></i></div>

<section>
  <h1 class="welcome-title">WELCOME TO BRIGHTPATH PHYSIOTHERAPY INC.</h1>
  <div class="welcome-photo" role="img" aria-label="Clinician standing outside a modern clinic building"></div>
  <div class="welcome-text">
    <p>We are Mississauga's premier physiotherapy and low intensity laser therapy specialists. We integrate low intensity laser therapy (laser therapy or cold laser therapy) with physiotherapy to safely and effectively treat a wide variety of musculoskeletal injuries and inflammatory conditions (i.e. back pain, arthritis, knee injuries, shoulder injuries, tendonitis, bursitis, repetitive strains, auto &amp; sports injuries). This clinically proven program can achieve remarkable results for acute injury and chronic pain patients and is painless.</p>
    <p>We Use a multi-faceted regime of clinically tested and proven protocols with one goal in mind: Get you better, faster. Our results-focused team includes registered physiotherapists, registered massage therapists, certified kinesiologists and certified athletic therapists.</p>
  </div>
</section>

<div class="divider" style="top:1024px"></div>

<section class="col" style="left:19px;top:1058px">
  <h2>Laser Treatment</h2>
  <div class="col-photo ph-laser" role="img" aria-label="Cold laser treatment on a foot"></div>
  <p>Donec quam felis, ultricies nec, pellentesque eu, pretium quis, sem. Nulla consequat massa quis enim. Donec pede justo, fringilla vel, aliquet nec, vulputate eget, arcu.</p>
  <p>In enim justo, rhoncus ut, imperdiet a, venenatis vitae, justo. Nullam dictum felis eu pede mollis pretium.</p>
  <a class="btn" style="top:513px">Read More...</a>
</section>

<section class="col" style="left:425px;top:1058px">
  <h2>Massage Treatment</h2>
  <div class="col-photo ph-massage" role="img" aria-label="Relaxing back massage"></div>
  <p>Donec quam felis, ultricies nec, pellentesque eu, pretium quis, sem. Nulla consequat massa quis enim. Donec pede justo, fringilla vel, aliquet nec, vulputate eget, arcu.</p>
  <p>In enim justo, rhoncus ut, imperdiet a, venenatis vitae, justo. Nullam dictum felis eu pede mollis pretium.</p>
  <a class="btn" style="top:513px">Read More...</a>
</section>

<section class="col" style="left:829px;top:1058px;height:560px">
  <h2>Blog</h2>
  <article class="post" style="top:40px">
    <h3>Dsena massa cum vceena tevsa bsse.</h3>
    <p>Arena massa cum vceena tevsa bsse metus massa cum vceena tevsa bsse metus.</p>
    <div class="share"><span>Like</span><span>3k</span><span>Share</span><span>316</span></div>
  </article>
  <article class="post" style="top:214px">
    <h3>Cfna massa cum vceena tevsa bsse.</h3>
    <p>Arena massa cum vceena tevsa bsse metus massa cum vceena tevsa bsse metus.</p>
    <div class="share"><span>Like</span><span>3k</span><span>Share</span><span>316</span></div>
  </article>
  <article class="post" style="top:395px">
    <h3>Dsena massa cum vceena tevsa bsse.</h3>
    <p>Arena massa cum vceena tevsa bsse metus massa cum vceena tevsa bsse metus.</p>
    <div class="share"><span>Like</span><span>3k</span><span>Share</span><span>316</span></div>
  </article>
</section>

<div class="divider" style="top:1644px"></div>

<section class="col" style="left:19px;top:1670px">
  <h2>Exercise Therapy</h2>
  <div class="col-photo ph-exercise" role="img" aria-label="Patient doing resistance band exercise with a trainer"></div>
  <p>Donec quam felis, ultricies nec, pellentesque eu, pretium quis, sem. Nulla consequat massa quis enim. Donec pede justo, fringilla vel, aliquet nec, vulputate eget, arcu.</p>
  <p>In enim justo, rhoncus ut, imperdiet a, venenatis vitae, justo. Nullam dictum felis eu pede mollis pretium.</p>
  <a class="btn" style="top:522px">Read More...</a>
</section>

<section class="col" style="left:425px;top:1670px">
  <h2>Insurance</h2>
  <div class="col-photo ph-insurance" role="img" aria-label="Health insurance paperwork"></div>
  <p>Donec quam felis, ultricies nec, pellentesque eu, pretium quis, sem. Nulla consequat massa quis enim. Donec pede justo, fringilla vel, aliquet nec, vulputate eget, arcu.</p>
  <p>In enim justo, rhoncus ut, imperdiet a, venenatis vitae, justo. Nullam dictum felis eu pede mollis pretium.</p>
  <a class="btn" style="top:522px">Read More...</a>
</section>

<section class="col" style="left:829px;top:1670px">
  <h2>Testimonials</h2>
  <div class="col-photo ph-testimonial" role="img" aria-label="Smiling senior patient"></div>
  <p>Donec quam felis, ultricies nec, pellentesque eu, pretium quis, sem. Nulla consequat massa quis enim. Donec pede justo, fringilla vel, aliquet nec, vulputate eget, arcu. Donec quam felis, ultricies nec, pellentesque ultricies nec, pellentesque.</p>
  <div class="cite">– Onullam Dictum</div>
  <a class="btn" style="top:522px">Read More...</a>
</section>

<footer>
  <div class="footer-rule"></div>
  <div class="footer-links">Home <span>|</span> About Us <span>|</span> Whiplash &amp; Auto Injuries <span>|</span> BrightPath In The News <span>|</span> Massage Therapy <span>|</span> Patient Forms <span>|</span> Employment Opportunities</div>
  <div class="footer-bar">
    <div class="copyright">Copyright © 2013 brightpathphysio</div>
    <div class="social"><i></i><i></i><i></i><i></i><i></i></div>
  </div>
</footer>

</div>
</body>
</html>
```